Dolsemk Business Cards

Business cards for real estate
Target Market(s)
Real estate
Industry/Entity Type
Real Estate Agent
Font styles to use
Serif
Requirements
Must have
- Photo and logo

```html
<!DOCTYPE html>
<html lang="en">
<head>
<meta charset="utf-8">
<title>Dolsemk Realty — Business Card</title>
<link rel="stylesheet" href="https://fonts.googleapis.com/css2?family=Tinos:ital,wght@0,400;0,700;1,400&display=swap">
<style>
  :root {
    --canvas-bg: #e4e0d9;
    --card-black: #0b0b0b;
    --card-black-soft: #262626;
    --gold: #c9a86a;
    --gold-light: #e3cb95;
    --white: #f7f7f5;
    --portrait-light: #fbfbfb;
    --portrait-mid: #d9dadd;
    --portrait-suit: #55575d;
  }
  * { margin: 0; padding: 0; box-sizing: border-box; }
  html, body {
    width: 1200px;
    height: 780px;
    overflow: hidden;
    background: var(--canvas-bg);
  }
  .card {
    position: absolute;
    left: 150px;
    top: 130px;
    width: 900px;
    height: 520px;
    overflow: hidden;
    background: var(--portrait-light);
    box-shadow: 0 14px 34px rgba(0,0,0,0.28);
    font-family: "Tinos", "Times New Roman", serif;
  }
  .card__portrait {
    position: absolute;
    left: 0;
    top: 0;
    width: 470px;
    height: 520px;
    background:
      radial-gradient(ellipse 60% 55% at 55% 85%, var(--portrait-suit) 0%, rgba(85,87,93,0.6) 45%, rgba(85,87,93,0) 75%),
      linear-gradient(160deg, var(--portrait-light) 0%, var(--portrait-mid) 100%);
  }
  .card__panel {
    position: absolute;
    inset: 0;
    width: 900px;
    height: 520px;
  }
  .card__content {
    position: absolute;
    left: 520px;
    top: 58px;
    width: 350px;
    color: var(--white);
  }
  .brand {
    display: flex;
    align-items: center;
    gap: 20px;
    margin-bottom: 44px;
  }
  .brand__dot {
    width: 58px;
    height: 58px;
    border-radius: 50%;
    background: var(--gold);
    flex: none;
  }
  .brand__name {
    font-weight: 400;
    color: var(--white);
    text-transform: uppercase;
    line-height: 1;
  }
  .brand__name-main {
    display: block;
    font-size: 44px;
    letter-spacing: 2px;
  }
  .brand__name-sub {
    display: block;
    font-size: 28px;
    letter-spacing: 11px;
    margin-top: 6px;
  }
  .person__name {
    font-size: 27px;
    letter-spacing: 1px;
    text-transform: uppercase;
  }
  .person__role {
    font-size: 21px;
    color: var(--gold);
    margin-bottom: 22px;
  }
  .address {
    font-size: 19px;
    line-height: 1.35;
    margin-bottom: 16px;
  }
  .contacts { list-style: none; }
  .contacts__item {
    display: flex;
    align-items: center;
    gap: 12px;
    font-size: 19px;
    line-height: 1.6;
  }
  .contacts__icon {
    width: 20px;
    height: 20px;
    flex: none;
  }
</style>
</head>
<body>
  <article class="card">
    <div class="card__portrait" role="img" aria-label="Portrait photo of the agent in a dark pinstripe suit and light blue tie against a white background"></div>

    <svg class="card__panel" viewBox="0 0 900 520" aria-hidden="true">
      <defs>
        <linearGradient id="panel-sheen" x1="0" y1="0" x2="1" y2="1">
          <stop offset="0" stop-color="var(--card-black-soft)"/>
          <stop offset="0.45" stop-color="var(--card-black)"/>
          <stop offset="1" stop-color="var(--card-black)"/>
        </linearGradient>
        <linearGradient id="gold-band" x1="0" y1="0" x2="0" y2="1">
          <stop offset="0" stop-color="var(--gold-light)"/>
          <stop offset="1" stop-color="var(--gold)"/>
        </linearGradient>
      </defs>
      <path class="panel__gold-edge" d="M444 0 C372 150 498 330 414 520 L900 520 L900 0 Z" fill="url(#gold-band)"/>
      <path class="panel__black" d="M458 0 C386 150 512 330 428 520 L900 520 L900 0 Z" fill="url(#panel-sheen)"/>
    </svg>

    <div class="card__content">
      <header class="brand">
        <span class="brand__dot"></span>
        <h1 class="brand__name">
          <span class="brand__name-main">Dolsemk</span>
          <span class="brand__name-sub">Realty</span>
        </h1>
      </header>

      <p class="person__name">Marcus Hale</p>
      <p class="person__role">Director</p>

      <p class="address">PO BOX 418, Harbour Lane<br>7th street, Carrowdale</p>

      <ul class="contacts">
        <li class="contacts__item">
          <span>(555) 204 3178</span>
          <svg class="contacts__icon" viewBox="0 0 20 20" aria-hidden="true">
            <circle cx="10" cy="10" r="9.5" fill="var(--gold)"/>
            <rect x="6.5" y="4.5" width="7" height="11" rx="1.5" fill="none" stroke="var(--card-black)" stroke-width="1.4"/>
            <line x1="9" y1="13.4" x2="11" y2="13.4" stroke="var(--card-black)" stroke-width="1.2"/>
          </svg>
        </li>
        <li class="contacts__item">
          <span>info@dolsemkrealty.com</span>
          <svg class="contacts__icon" viewBox="0 0 20 20" aria-hidden="true">
            <circle cx="10" cy="10" r="9.5" fill="var(--gold)"/>
            <rect x="5" y="6.5" width="10" height="7" fill="none" stroke="var(--card-black)" stroke-width="1.3"/>
            <polyline points="5,6.5 10,10.8 15,6.5" fill="none" stroke="var(--card-black)" stroke-width="1.3"/>
          </svg>
        </li>
        <li class="contacts__item">
          <span>www.dolsemkrealty.com</span>
          <svg class="contacts__icon" viewBox="0 0 20 20" aria-hidden="true">
            <circle cx="10" cy="10" r="9.5" fill="var(--gold)"/>
            <circle cx="10" cy="10" r="5.2" fill="none" stroke="var(--card-black)" stroke-width="1.2"/>
            <ellipse cx="10" cy="10" rx="2.2" ry="5.2" fill="none" stroke="var(--card-black)" stroke-width="1.1"/>
            <line x1="4.8" y1="10" x2="15.2" y2="10" stroke="var(--card-black)" stroke-width="1.1"/>
          </svg>
        </li>
      </ul>
    </div>
  </article>
</body>
</html>
```